QTR Newsletter

QTR provides mortgage processing outsource services to Mortgage Lenders in Australia and New Zealand. The company employs approximately 300 staff based in offices in Sydney, Melbourne, Brisbane, Adelaide and Perth in Australia and Auckland, New Zealand.
The company acquired a similar and much larger business in 2012 which is being integrated into the one business.
The objectives of a newsletter are to:
- Support the development of the company culture
- Develp a sense of "one team"
- Provide a communication forum for management and staff
I am seeking design options for the newsletter. We will develop/include specific content which will likley evolve over time.
A copy of the company brand gudelines and logo is attached for reference. Our website is currently going through a redesign. Additional information can be provided on request.

Target Market(s)

The target market for the newsletter is staff. This is a diverse group in terms of locations, age, gender, occupations etc.

Industry/Entity Type

Communication

Requirements
Must have
• Information to be included in the newsletter should include:
- Business results (activity, volumes, performance to budget)
- Client news section (recent developments, client profiling etc)
- New initiatives (update on key projects and new business initiatives, initiatives roadmap)
- Office news (news section for each office including new employees, team profile of the month, report on social events)
- CEO report

```html
<!DOCTYPE html>
<html lang="en">
<head>
<meta charset="utf-8">
<title>The Buzz — Newsletter Spread</title>
<link rel="stylesheet" href="https://fonts.googleapis.com/css2?family=Carlito:wght@400;700&family=Crimson+Text:wght@400;600&display=swap">
<style>
  :root{
    --ink:#1b1b1b;
    --body:#2a2a2a;
    --rule:#8a8a8a;
    --frame:#9a9a9a;
    --accent-blue:#2a6fa8;
    --accent-cyan:#2e8bbd;
    --accent-green:#a8b43a;
    --news-green:#afb832;
    --panel-beige:#efefe6;
    --page-grey:#eceeef;
    --pie-teal:#2e7ea0;
    --pie-coral:#f0644e;
    --pie-green:#a9bb3b;
    --pie-grey:#d9dcd6;
    --bar-aqua:#6cc3c7;
  }
  *{margin:0;padding:0;box-sizing:border-box}
  html,body{width:1200px;height:849px;overflow:hidden;background:#fff}
  body{position:relative;font-family:"Carlito",Calibri,sans-serif;color:var(--body)}
  .abs{position:absolute}
  .page{position:absolute;top:43px;height:767px;border:1px solid var(--frame)}
  .page--left{left:41px;width:518px;background:#fff}
  .page--right{left:643px;width:518px;background:var(--page-grey)}
  .headline{font-weight:700;color:var(--ink);letter-spacing:-.5px;line-height:1}
  .copy{font-size:10px;line-height:12.1px;text-align:justify}
  .copy p+p{text-indent:12px}
  .dropcap{float:left;font-size:40px;line-height:32px;color:var(--accent-blue);margin:1px 3px 0 0}
  .ceo-photo{float:right;width:88px;height:97px;margin:3px -7px 4px 10px;background:linear-gradient(160deg,#c9ccd0,#8e939b 60%,#6e7680)}
  .section-rule{left:76px;top:399px;width:426px;height:1px;background:var(--rule)}
  .section-title{left:76px;top:424px;font-size:16px;letter-spacing:4.2px;color:var(--ink)}
  .results-panel{left:76px;top:452px;width:435px;height:315px;background:var(--panel-beige)}
  .quarter-label{color:var(--accent-green);font-size:12px}
  .chart-label{font-size:10px;color:var(--ink);text-align:center;width:40px}
  .sub-label{font-size:9.5px;letter-spacing:.6px;color:var(--ink)}
  .sub-rule{height:1px;background:var(--rule)}
  .region-map{left:96px;top:625px;width:218px;height:122px;background:linear-gradient(180deg,#d4d4cc,#bdbdb5)}
  .cover-photo{left:678px;top:0;width:258px;height:222px;background:linear-gradient(175deg,#3a5f86 0%,#7b95ad 40%,#d8b878 70%,#3d5a78 100%)}
  .subhead{font-size:9.8px;font-weight:700;color:var(--accent-blue);margin:10px 0 1px}
  .news-box{left:967px;top:82px;width:167px;height:451px;background:var(--news-green);padding:22px 20px}
  .news-title{color:#fff;font-size:29px;font-weight:700;line-height:25px;margin-bottom:20px}
  .news-copy{font-size:15.2px;line-height:18px;color:#2b2f1f}
  .office-box{left:968px;top:558px;width:167px;height:231px;background:#fff;border:1px solid var(--frame)}
  .office-photo{left:987px;top:552px;width:126px;height:66px;background:linear-gradient(135deg,#f3f1ec,#d9d2c3 60%,#c7b79b)}
  .office-title{font-size:14.5px;font-weight:700;line-height:13px;color:var(--accent-cyan)}
  .footer{top:819px;font-family:"Crimson Text",Georgia,serif;font-size:12.5px;color:var(--ink);letter-spacing:.3px}
  .footer b{font-family:"Carlito",Calibri,sans-serif;font-size:13px}
</style>
</head>
<body>

<div class="page page--left"></div>
<div class="page page--right"></div>

<!-- Page 2 : CEO report -->
<h1 class="abs headline" style="left:75px;top:74px;font-size:50px">CEO Report</h1>
<div class="abs copy" style="left:76px;top:138px;width:434px">
  <div class="ceo-photo" role="img" aria-label="Portrait photo of the chief executive"></div>
  <p><span class="dropcap">W</span>hen et am rest, sent eos simaximet optur?Pudiorr untiusandi acerit omnia ducienietus. Agnihit iuresto rempost, nonse cor autat voluptio ipsus ipsamusdae nonetur, soluptatus.Odiat. Dia sit, officiatur, inihil id etur res estio dolorerrorem et, con cus, ipiet aute vel et es alit init quas aut venisitatum raes inum excepedia et exped quiaectem quae qui dolore omnis aceritium rempos nat eation res es explandes molor samendit haribusam et evelend isquame ndempos volut is et accus molut pos aliqui ad maionet uritates dolupta sperferum eicae lautem. Ut fugit, optaspellab ipsus eicto quam, consequ atectamet, consequam, te illictem ant voluptis magnat eatestio vent.</p>
  <p>Exero volenem hitaquas errorio. Ga. Ut aute cupti cusda am, sitem sumque quid quia consequo ma inia essi ut enis et pratur accae quaerias aliqui con explique susam estianihite aut et verovit venduntur, inulloreiur sumet, ius aut andandi nes est verepudit quibus rehenti usant.</p>
  <p>Excea excea sitiunt. Osa eum doluptio consed ex ea dit aut ex eumquam rem rerfercid quiassim sitaes illorec aecerum consed quae nienimo loreperum dempor aut voluptas dolor autem. Et illorae volorio molore cuptatiatur aut reriat pos et estotae rspicab oriosseque providerum utatis et voluptur? Odia sumqui beaquam dolesti quiam autem name eos estem ex eve estorroriame pa quas que dolupta nam aris atur sit, ea quae pores min ea quate vit min nonem. Nequasperias quidenti que voluptatis aliquo es erro est re expliquiande rehent expeles audi test, occaborpor maxim recest, offici ius at volupta quam ducitius.</p>
</div>

<div class="abs section-rule"></div>
<h2 class="abs section-title" style="font-weight:400">RESULTS DRIVEN</h2>

<section class="abs results-panel"></section>
<div class="abs copy" style="left:109px;top:475px;width:172px;font-size:9.8px;line-height:12.2px;text-align:left">
  <span class="quarter-label">THIS QUARTER</span> Exero volenem hitaquas errorio. Ga. Ut aute cupti cusda am, sitem sumque quid quia consequo ma inia essi ut enis et pratur accae quaerias aliqui con explique susam estianihite aut et verovit venduntur, inulloreiur sumet, ius aut andandi nes est verepudit quibus rehenti usant.
</div>

<svg class="abs" style="left:326px;top:478px" width="160" height="48" viewBox="0 0 160 48" aria-label="Pie charts for 2008, 2010 and 2012">
  <g transform="translate(23,23)">
    <circle r="21" fill="var(--pie-teal)"/>
    <path d="M0 0 L0 -21 A21 21 0 0 1 20 6 Z" fill="var(--pie-green)"/>
    <path d="M0 0 L20 6 A21 21 0 0 1 -4 21 Z" fill="var(--pie-coral)"/>
    <path d="M0 0 L-10 -18 A21 21 0 0 1 0 -21 Z" fill="var(--pie-grey)"/>
  </g>
  <g transform="translate(79,23)">
    <circle r="21" fill="var(--pie-coral)"/>
    <path d="M0 0 L0 -21 A21 21 0 0 1 14 16 L0 0 Z" fill="var(--pie-teal)"/>
    <path d="M0 0 L0 -21 A21 21 0 0 1 11 -18 Z" fill="var(--pie-green)"/>
    <path d="M0 0 L-7 -20 A21 21 0 0 1 0 -21 Z" fill="var(--pie-grey)"/>
  </g>
  <g transform="translate(135,23)">
    <circle r="21" fill="var(--pie-coral)"/>
    <path d="M0 0 L-6 -20 A21 21 0 0 1 8 -19 Z" fill="var(--pie-green)"/>
    <path d="M0 0 L-12 -17 A21 21 0 0 1 -6 -20 Z" fill="var(--pie-grey)"/>
    <path d="M0 0 L8 -19 A21 21 0 0 1 12 -17 Z" fill="var(--pie-teal)"/>
  </g>
</svg>
<div class="abs chart-label" style="left:329px;top:530px">2008</div>
<div class="abs chart-label" style="left:385px;top:530px">2010</div>
<div class="abs chart-label" style="left:441px;top:530px">2012</div>

<div class="abs sub-label" style="left:98px;top:600px">BY REGION</div>
<div class="abs sub-rule" style="left:96px;top:616px;width:212px"></div>
<div class="abs sub-label" style="left:366px;top:600px">CHANNELS</div>
<div class="abs sub-rule" style="left:365px;top:616px;width:121px"></div>

<div class="abs region-map" role="img" aria-label="World map with office location markers"></div>

<svg class="abs" style="left:368px;top:638px" width="112" height="102" viewBox="0 0 112 102" aria-label="Channels bar graphic">
  <rect x="2" y="20" width="16" height="60" fill="var(--pie-grey)"/>
  <rect x="2" y="20" width="16" height="12" fill="var(--pie-coral)"/>
  <rect x="2" y="32" width="16" height="12" fill="var(--bar-aqua)"/>
  <rect x="2" y="44" width="16" height="12" fill="var(--pie-green)"/>
  <rect x="2" y="68" width="16" height="12" fill="var(--pie-teal)"/>
  <path d="M30 6 H104 L110 13 L104 20 H30 Z" fill="var(--pie-coral)"/>
  <path d="M30 28 H104 L110 35 L104 42 H30 Z" fill="var(--bar-aqua)"/>
  <path d="M30 50 H104 L110 57 L104 64 H30 Z" fill="var(--pie-green)"/>
  <path d="M30 71 H104 L110 78 L104 85 H30 Z" fill="var(--pie-grey)"/>
  <path d="M30 88 H104 L110 95 L104 102 H30 Z" fill="var(--pie-teal)"/>
  <path d="M18 26 L30 13 M18 38 L30 35 M18 50 L30 57 M18 62 L30 78 M18 74 L30 95" stroke="#9aa0a0" stroke-width="1.2" fill="none"/>
</svg>

<!-- Page 3 : Our clients -->
<div class="abs cover-photo" role="img" aria-label="Photo of a glass office tower against a sunlit sky"></div>
<h1 class="abs headline" style="left:677px;top:230px;font-size:47px">Our Clients</h1>
<div class="abs copy" style="left:678px;top:292px;width:260px">
  <p><span class="dropcap">K</span>hen et am rest, sent eos simaximet optur?Pudiorr untiusandi acerit omnia ducienietus. Agnihit iuresto rempost, nonse cor autat voluptio ipsus ipsamusdae nonetur, soluptatus.Odiat. Dia sit, officiatur, inihil id etur res estio dolorerrorem et, con cus, ipiet aute vel et es alit init quas aut venisitatum raes inum excepedia et exped quiaectem quae qui dolore accus molut pos aliqui ad maionet uritates dolupta sperferum eicae lautem. Ut fugit, optaspellab ipsus eicto quam, consequ atectamet, conseq illictem ant voluptis magnat eatestio vent.</p>
  <div class="subhead">SUBHEAD ABOUT CLIENT 1</div>
  <p>Exero volenem hitaquas errorio. Ga. Ut aute cupti cusda am, sitem sumque quid quia consequo ma inia essi ut enis et pratur accae quaerias aliqui con explique susam estianihite aut et verovit venduntur, inulloreiur sumet, ius aut andandi nes est verepudit quibus rehenti usant.</p>
  <p>Excea excea sitiunt. Osa eum doluptio consed ex ea dit aut ex eumquam rem rerfercid quiassim sitaes illorec aecerum consed quae nienimo loreperum dempor aut voluptas dolor autem. Et illorae volorio molore cuptatiatur aut reriat pos et estotae rspicab oriosseque providerum utatis et voluptur? Odia sumqui beaquam dolesti quiam autem name eos estem ex eve estorroriame pa quas que dolupta nam aris atur sit, ea quae pores min ea quate vit min nonem. Nequasperias quidenti que voluptatis aliquo es erro est re expliquiande rehent expeles audi test, occaborpor maxim recest, offici ius at volupta quam ducitius. Exero volenem hitaquas errorio. Ga. Ut aute cupti cusda am, sitem sumque quid quia consequo ma inia essi ut enis et pratur accae quaerias aliqui con explique susam estianihite aut et verovit venduntur, inulloreiur sumet, ius aut andandi nes est verepudit quibus rehenti usant.</p>
  <div class="subhead" style="margin-top:12px">SUBHEAD ABOUT CLIENT2</div>
  <p>Excea excea sitiunt. Osa eum doluptio consed ex ea dit aut ex eumquam rem rerfercid quiassim sitaes illorec aecerum consed quae nienimo loreperum dempor aut voluptas dolor autem. Et illorae volorio molore cuptatiatur aut reriat pos et estotae beaquam dolesti quiam autem name eos estem ex eve e.</p>
</div>

<aside class="abs news-box">
  <h2 class="news-title">MORE<br>NEWS</h2>
  <p class="news-copy">Agnihit iuresto rempost, nonse cor autat voluptio ipsus ipsamusdae nonetur, soluptatus.Odiat. Dia sit, officiatur, inihil id etur res estio dolorerrorem et, con cus, ipiet aute dolore omnis ac dit haribusam et dit haribusam et eritium rempos nat eation res es explandes molor samendit haribusam et evelend isquame ndempos volut is et</p>
</aside>

<aside class="abs office-box"></aside>
<div class="abs office-photo" role="img" aria-label="Photo of architectural plans, rolled drawings and a pen"></div>
<h3 class="abs office-title" style="left:987px;top:627px">OFFICE<br>RENOVATION</h3>
<p class="abs copy" style="left:987px;top:656px;width:128px;font-size:9.6px;line-height:11.8px;text-align:left">Agnihit iuresto rempost, nonse cor autat voluptio ipsus ipsamusdae nonetur, soluptatus.Odiat. Dia sit, officiatur, inihil id etur res aceritium rempos nat eation res es explandes molor samendit haribusam et evelend isquame ndempos volut is et</p>

<!-- Folios -->
<div class="abs footer" style="left:41px"><b>2</b>&nbsp;&nbsp;THE BUZZ &nbsp;•&nbsp; FEB 12, 2013</div>
<div class="abs footer" style="right:39px">THE BUZZ &nbsp;•&nbsp; FEB 12, 2013&nbsp;&nbsp;<b>3</b></div>

</body>
</html>
```